Creation of a construction/bricklaying business website

Following the template format of "Wendmoor 2", the following content would need to be included:
1. Landing page with 3 tiles that go to their own pages.
- Landing page to include background photo and description of services offered.
2. 3 tiles to include:
a) "Contact Us For A Free Quote or Friendly Discussion" Form (middle tile)
b) Case Studies and Testimonials
c) Certifications and Professional Membership
- Design logo to be used from previous PixelHarbor project. Example of logo attached below, please access full JPG files from our account.

Target Market(s)

Prospective clients seeking construction work (bricklaying speciality)

Industry/Entity Type

Residential Construction

Coding

Coded - Design and coding required

Number of Pages Required

4 page

Font styles to use
Sans Serif

Colors

Designer to choose colors to be used in the design.

Requirements
Must have
• Following the template format of "Wendmoor 2", the following content would need to be included:
• 1. Landing parent page with 3 tiles that go to the 3 child pages.
• - Landing page to include background photo and description of services offered.
• 2. 3 tiles to include:
• a) "Contact Us For A Free Quote or Friendly Discussion" Form (middle tile)
• b) Case Studies and Testimonials (first tile / left side)
• c) Certifications and Professional Memberships (third tile / right side) (This should include logos of the relevant organisations being displayed. Specifically QLT and the Keystone Pact QLT).
• - Design logo to be used from previous PixelHarbor project. Example of logo attached below, please access full JPG files from our account.
Nice to have
• Sleek and modern feel.
• Approachable in terms of how people can contact the company for a quote.
• Traditional pictures to give credibility and comfort around choosing this company.
Should not have
• Cheesy pictures
• Over-complicated
• Simple to use
• Easy URL domain name

```html
<!DOCTYPE html>
<html lang="en">
<head>
<meta charset="utf-8">
<title>R.T. Hale Construction</title>
<link href="https://fonts.googleapis.com/css2?family=Montserrat:wght@400;600;700;800&family=Open+Sans:wght@400;600;700&display=swap" rel="stylesheet">
<style>
:root{
  --blue:#1451a3;
  --blue-dark:#0e3f82;
  --ink:#1c1c1c;
  --text:#555;
  --muted:#8a8a8a;
  --line:#d9d9d9;
  --white:#fff;
  --band:#efefef;
  --footer:#2b2b2b;
  --footer-text:#bdbdbd;
}
*{box-sizing:border-box;margin:0;padding:0}
html,body{width:1200px;height:3636px;overflow:hidden}
body{font-family:"Open Sans",Arial,sans-serif;color:var(--text);background:var(--white);position:relative}
.wrap{position:absolute;left:160px;width:880px}
h1,h2,h3,.num,.nav a,.brand{font-family:"Montserrat",Arial,sans-serif}

/* header */
.site-header{position:absolute;top:0;left:0;width:1200px;height:80px;background:var(--white)}
.brand{position:absolute;left:160px;top:22px;font-weight:800;font-size:27px;color:var(--blue);line-height:1}
.brand small{display:block;font-size:9px;font-weight:700;letter-spacing:1.5px;margin-top:3px;color:var(--ink)}
.nav{position:absolute;left:500px;top:30px;display:flex;font-size:12.5px;font-weight:600}
.nav a{color:var(--ink);text-decoration:none;padding:0 26px;position:relative}
.nav a+a:before{content:"|";position:absolute;left:-2px;color:var(--muted)}
.nav a.active{color:var(--blue)}
.nav a.active:after{content:"";position:absolute;left:50%;top:-30px;width:2px;height:16px;background:var(--blue)}

/* hero */
.hero{position:absolute;top:80px;left:0;width:1200px;height:616px;background:linear-gradient(180deg,#5c6470 0%,#3e4752 55%,#2c333c 100%)}
.hero .shade{position:absolute;inset:0;background:linear-gradient(90deg,rgba(20,26,34,.65),rgba(20,26,34,.2))}
.hero-frame{position:absolute;left:160px;top:140px;width:216px;height:308px;border:2px solid rgba(255,255,255,.85)}
.hero-copy{position:absolute;left:190px;top:200px;color:var(--white)}
.hero-copy .num{font-size:36px;font-weight:700}
.hero-copy .kicker{margin:12px 0 0 52px;font-family:"Montserrat",sans-serif;font-weight:600;font-size:18px}
.hero-copy h1{margin:8px 0 0 52px;font-size:58px;line-height:66px;font-weight:800;letter-spacing:.5px}
.arrow{position:absolute;top:270px;width:28px;height:36px}
.hero .dots{position:absolute;left:162px;top:480px;display:flex;gap:5px}
.hero .dots i{width:10px;height:10px;background:rgba(255,255,255,.5)}
.hero .dots i:first-child{background:var(--blue)}

/* services band */
.services{position:absolute;top:696px;left:0;width:1200px;height:172px;background:var(--blue)}
.services ul{position:absolute;left:160px;width:880px;top:32px;display:flex;list-style:none}
.services li{flex:1;text-align:center;color:var(--white);font-family:"Montserrat",sans-serif;font-weight:700;font-size:13px;border-left:1px solid rgba(255,255,255,.4);height:110px}
.services li:first-child{border-left:0}
.services svg{display:block;margin:6px auto 10px;width:66px;height:66px}
.services .arrow{top:66px;width:18px;height:26px}

/* section heads */
.sec-head .num{font-size:36px;font-weight:700;color:var(--ink);line-height:1}
.sec-head .sub{font-size:14px;color:var(--muted);margin-top:4px}
.sec-head h2{font-size:24px;font-weight:800;color:var(--ink);margin-top:18px;letter-spacing:.5px}

/* cases */
.cases{top:930px}
.case-grid{display:flex;gap:32px;margin-top:30px}
.case{width:272px}
.case .photo{height:184px}
.case h3{font-size:14.5px;color:var(--blue);font-weight:700;margin-top:24px}
.case p{font-size:11.5px;line-height:19px;margin-top:8px}
.btn{display:inline-block;background:var(--blue);color:var(--white);font-family:"Montserrat",sans-serif;font-weight:700;font-size:11px;padding:9px 20px;margin-top:18px}
.rule{position:absolute;top:1447px;left:0;width:1200px;height:2px;background:#e6e6e6}

/* testimonials */
.testis{top:1484px}
.testi-grid{display:flex;gap:52px;margin-top:48px;padding:0 2px}
.testi{width:260px;height:303px;border:3px solid var(--blue);position:relative;text-align:center;padding:50px 24px 0}
.testi .q{position:absolute;font-family:Georgia,serif;font-weight:700;font-size:110px;line-height:1;color:var(--blue);background:var(--white);padding:0 4px;height:60px;overflow:visible}
.testi .q.open{left:-14px;top:-24px}
.testi .q.close{right:-14px;bottom:-24px;line-height:.6;height:50px}
.avatar{width:80px;height:80px;border-radius:50%;margin:0 auto;background:radial-gradient(circle at 50% 40%,#d9d4cf,#9ea3aa)}
.testi p{font-size:11px;line-height:20px;margin-top:18px;color:#444}
.testi .who{font-family:"Montserrat",sans-serif;font-weight:700;font-size:11.5px;color:var(--ink);margin-top:12px}
.testi .date{font-size:11px;margin-top:2px}
.pager{position:absolute;top:1982px;left:583px;display:flex;gap:4px}
.pager i{width:9px;height:9px;background:#243a5e}

/* contact */
.contact{position:absolute;top:2060px;left:0;width:1200px;height:454px;background:linear-gradient(180deg,#3a4553 0%,#56606c 55%,#3c4553 100%)}
.contact .shade{position:absolute;inset:0;background:rgba(30,38,50,.45)}
.contact .sec-head .num,.contact .sec-head h2,.contact .sec-head .sub{color:var(--white)}
.contact .wrap{top:84px}
.fields{display:flex;gap:28px;margin-top:44px}
.field{flex:1;border-bottom:1px solid rgba(255,255,255,.75);color:var(--white);font-size:11.5px;padding-bottom:6px}
.field.full{margin-top:26px;padding-bottom:40px}
.contact .btn{margin-top:28px;padding:9px 28px}

/* certifications */
.certs{top:2576px}
.cert-media{position:absolute;left:0;top:156px;width:326px;height:230px;background:radial-gradient(ellipse at 40% 50%,#f2d34a 0%,#e8c030 30%,#f4f4f4 62%,#fff 80%)}
.cert-body{position:absolute;left:393px;top:160px;width:487px;border-left:3px solid var(--blue);padding-left:20px}
.cert-body h3{font-size:19px;font-weight:800;color:var(--ink);letter-spacing:.3px}
.cert-body h3 span{color:var(--blue)}
.cert-body .lead{font-size:12.5px;line-height:21px;color:#333;margin-top:14px}
.cert-body .small{font-size:10.5px;line-height:18px;color:var(--muted);margin-top:12px}
.perks-title{position:absolute;top:440px;left:0;font-family:"Montserrat",sans-serif;font-weight:700;font-size:13px;color:var(--ink)}
.perks{position:absolute;top:480px;left:0;width:880px;display:grid;grid-template-columns:432px 404px;column-gap:44px;row-gap:10px;list-style:none}
.perks li{border:1px solid var(--line);height:30px;font-size:11px;padding:6px 14px 0 28px;position:relative}
.perks li:before{content:"";position:absolute;left:13px;top:11px;width:6px;height:6px;border-radius:50%;background:var(--blue)}

/* partner band */
.partners{position:absolute;top:3241px;left:0;width:1200px;height:129px;background:var(--band)}
.partners .badge{position:absolute;top:36px}

/* footer */
.site-footer{position:absolute;top:3370px;left:0;width:1200px;height:266px;background:var(--footer);color:var(--footer-text);font-size:11px}
.site-footer h4{font-family:"Montserrat",sans-serif;font-size:12.5px;color:var(--white);font-weight:600;letter-spacing:.3px}
.col{position:absolute;top:48px}
.col p{line-height:19px;margin-top:14px}
.col ul{list-style:none;margin-top:14px}
.col li{line-height:19px}
.col li:before{content:"› ";color:var(--footer-text)}
.vline{position:absolute;top:46px;width:1px;height:130px;background:#4a4a4a}
.social{display:flex;gap:7px;margin-top:8px}
.social i{width:16px;height:16px;border-radius:50%;background:var(--blue)}
.email-box{width:258px;height:36px;background:#444;margin-top:22px;color:#aaa;padding:10px 14px}
.signup{display:inline-block;background:var(--blue);color:var(--white);font-family:"Montserrat",sans-serif;font-weight:700;font-size:11px;padding:9px 22px;margin-top:16px}
.copy{position:absolute;left:160px;top:3600px;font-size:10.5px;color:var(--footer-text);border-top:1px solid #4a4a4a;width:880px;padding-top:8px}
</style>
</head>
<body>

<header class="site-header">
  <div class="brand">R.T. Hale<small>CONSTRUCTION LTD</small></div>
  <nav class="nav">
    <a class="active">Contact Us</a><a>Case Studies</a><a>Testimonials</a><a>Certifications</a><a>Membership</a>
  </nav>
</header>

<section class="hero">
  <div class="shade" role="img" aria-label="Photo of a modern white apartment block against the sky"></div>
  <div class="hero-frame"></div>
  <div class="hero-copy">
    <div class="num">01.</div>
    <div class="kicker">R.T. Hale Construction</div>
    <h1>WELCOME<br>TO R. T. HALE</h1>
  </div>
  <svg class="arrow" style="left:108px" viewBox="0 0 28 36"><path d="M20 4 8 18l12 14" fill="none" stroke="#fff" stroke-width="3"/></svg>
  <svg class="arrow" style="left:1046px" viewBox="0 0 28 36"><path d="M8 4l12 14L8 32" fill="none" stroke="#fff" stroke-width="3"/></svg>
  <div class="dots"><i></i><i></i><i></i></div>
</section>

<section class="services">
  <svg class="arrow" style="left:110px" viewBox="0 0 18 26"><path d="M14 3 5 13l9 10" fill="none" stroke="#fff" stroke-width="2.5"/></svg>
  <svg class="arrow" style="left:1070px" viewBox="0 0 18 26"><path d="M4 3l9 10-9 10" fill="none" stroke="#fff" stroke-width="2.5"/></svg>
  <ul>
    <li><svg viewBox="0 0 66 66" fill="none" stroke="#fff" stroke-width="3"><rect x="14" y="14" width="20" height="46"/><rect x="34" y="28" width="18" height="32"/><path d="M19 22h4M27 22h2M19 32h4M27 32h2M19 42h4M27 42h2M39 36h8M39 46h8M8 60h50"/></svg>Extensions</li>
    <li><svg viewBox="0 0 66 66" fill="#fff"><path d="M33 8 6 32h8v26h15V42h8v16h15V32h8z"/></svg>New Build</li>
    <li><svg viewBox="0 0 66 66" fill="none" stroke="#fff" stroke-width="3"><rect x="8" y="14" width="50" height="40"/><path d="M8 24h50M8 34h50M8 44h50M24 14v10M42 14v10M16 24v10M33 24v10M50 24v10M24 34v10M42 34v10M16 44v10M33 44v10M50 44v10"/></svg>Garden Walls</li>
    <li><svg viewBox="0 0 66 66" fill="#fff"><path d="M6 46 46 18l14 8-40 28z"/><rect x="40" y="8" width="6" height="16" transform="rotate(35 43 16)"/></svg>Plastering</li>
    <li><svg viewBox="0 0 66 66" fill="none" stroke="#fff" stroke-width="3"><path d="M8 56h40M8 46h40M8 36h30M20 36v10M34 36v10M14 46v10M28 46v10M42 46v10M40 30l16-18M52 8l8 8"/></svg>Brickwork</li>
    <li><svg viewBox="0 0 66 66" fill="#fff"><path d="M14 32a19 19 0 0 1 38 0z"/><rect x="10" y="32" width="46" height="5"/><rect x="31" y="9" width="4" height="10"/><path d="M18 60c0-10 7-16 15-16s15 6 15 16z"/></svg>Groundworks</li>
  </ul>
</section>

<section class="wrap cases">
  <div class="sec-head"><div class="num">02.</div><div class="sub">R.T. Hale Construction</div><h2>CASE STUDIES</h2></div>
  <div class="case-grid">
    <article class="case"><div class="photo" role="img" aria-label="Photo of a glass office tower lit at dusk" style="background:linear-gradient(180deg,#2f6fc4,#6d8fb8 60%,#3a3a3a)"></div><h3>Riverside mixed-use block</h3><p>Full brickwork and structural shell for a six storey scheme delivered on time, on budget and with careful site management.</p><span class="btn">Learn More ›</span></article>
    <article class="case"><div class="photo" role="img" aria-label="Photo of tower blocks and cranes beside a green field" style="background:linear-gradient(180deg,#cfe0f2,#b9c7d6 55%,#7fae4a 75%,#5d9a34)"></div><h3>Meadowside housing phase</h3><p>Groundworks, foundations and facing brick for forty family homes built alongside a busy working site and new roads.</p><span class="btn">Learn More ›</span></article>
    <article class="case"><div class="photo" role="img" aria-label="Photo of a city skyline with high-rise towers under blue sky" style="background:linear-gradient(180deg,#7ea8da,#b8c9dc 55%,#8d8f94)"></div><h3>Harbour view apartments</h3><p>Extension and repointing works across three linked residential towers, finished with minimal disruption to residents.</p><span class="btn">Learn More ›</span></article>
  </div>
</section>
<div class="rule"></div>

<section class="wrap testis">
  <div class="sec-head"><div class="num">03.</div><div class="sub">R.T. Hale Construction</div><h2>TESTIMONIAL</h2></div>
  <div class="testi-grid">
    <article class="testi"><span class="q open">“</span><div class="avatar" role="img" aria-label="Portrait photo of the client"></div><p>We pride ourselves on attention to detail, pride in our completed project and client satisfaction. We believe in full transparency and this is reflected in the jobs we quote for you.</p><div class="who">MARA ELLISON</div><div class="date">7-Aug-2018</div><span class="q close">”</span></article>
    <article class="testi"><span class="q open">“</span><div class="avatar" role="img" aria-label="Portrait photo of the client"></div><p>We pride ourselves on attention to detail, pride in our completed project and client satisfaction. We believe in full transparency and this is reflected in the jobs we quote for you.</p><div class="who">MARA ELLISON</div><div class="date">7-Aug-2018</div><span class="q close">”</span></article>
    <article class="testi"><span class="q open">“</span><div class="avatar" role="img" aria-label="Portrait photo of the client"></div><p>We pride ourselves on attention to detail, pride in our completed project and client satisfaction. We believe in full transparency and this is reflected in the jobs we quote for you.</p><div class="who">MARA ELLISON</div><div class="date">7-Aug-2018</div><span class="q close">”</span></article>
  </div>
</section>
<div class="pager"><i></i><i></i><i></i></div>

<section class="contact">
  <div class="shade" role="img" aria-label="Photo of a city skyline of glass towers at dusk"></div>
  <div class="wrap">
    <div class="sec-head"><div class="num">04.</div><div class="sub">R.T. Hale Construction</div><h2>CONTACT US</h2></div>
    <div class="fields"><div class="field">Full Name :</div><div class="field">E-mail :</div><div class="field">Number :</div><div class="field">Post Code :</div></div>
    <div class="field full">Description of the job required :</div>
    <span class="btn">Submit ›</span>
  </div>
</section>

<section class="wrap certs" style="height:640px">
  <div class="sec-head"><div class="num">05.</div><div class="sub">R.T. Hale Construction</div><h2>CERTIFICATIONS AND PROFESSIONAL MEMBERSHIPS</h2></div>
  <div class="cert-media" role="img" aria-label="Photo of a yellow hard hat resting on rolled building plans"></div>
  <div class="cert-body">
    <h3>R.T.<span>HALE CONSTRUCTION</span></h3>
    <p class="lead">R.T. Hale Construction is a registered company with the Quality League of Trades (QLT). The QLT has a strict membership criteria and dispute resolution service which gives our clients the confidence.</p>
    <p class="small">To be a member of the QLT a company must be inspected by QLT inspectors as well as site building inspectors. QLT staff will be present onsite to inspect our work as well as conducting interviews with the owner of R.T. Hale Construction and our employees. This membership provides key benefits for our clients. Specifically, being a member of QLT allows R.T. Hale Construction to have regional building office (RBO) approval.</p>
  </div>
  <div class="perks-title">QLT MEMBERSHIP MEANS THAT R.T. HALE CONSTRUCTION LTD :</div>
  <ul class="perks">
    <li>Has a minimum of twelve months trading.</li>
    <li>Have provided a professional reference.</li>
    <li>Have passed credit checks, public record and director checks.</li>
    <li>Has Public and Employer (if applicable) Liability Insurance.</li>
    <li>Has Public and Employer (if applicable) Liability Insurance.</li>
    <li>Has signed up to the QLT Code of Practice.</li>
  </ul>
</section>

<section class="partners" aria-label="Partner memberships">
  <svg class="badge" style="left:202px" width="144" height="60" role="img" aria-label="QLT membership badge"><rect width="144" height="60" fill="#d8262b"/></svg>
  <svg class="badge" style="left:452px" width="130" height="64" role="img" aria-label="Keystone Pact QLT badge"><rect width="130" height="64" fill="#c8202a"/></svg>
  <svg class="badge" style="left:690px" width="74" height="72" role="img" aria-label="Regional Building Office badge"><rect width="74" height="72" fill="#e07a1e"/></svg>
  <svg class="badge" style="left:868px" width="124" height="44" role="img" aria-label="Northline Survey badge"><rect y="6" width="124" height="34" rx="17" fill="#e53935"/></svg>
</section>

<footer class="site-footer">
  <div class="col" style="left:160px;width:260px">
    <h4><svg width="12" height="15" viewBox="0 0 12 15" style="vertical-align:-2px;margin-right:6px"><path d="M6 0a6 6 0 0 0-6 6c0 4.5 6 9 6 9s6-4.5 6-9a6 6 0 0 0-6-6zm0 8.5A2.5 2.5 0 1 1 6 3.5a2.5 2.5 0 0 1 0 5z" fill="#fff"/></svg>GET IN TOUCH</h4>
    <p>Unit 4, Mill Lane Works<br>Harrowfield Business Park<br>Email : info@rthaleconstruction.com<br>Contact no: +1 555 010 2299</p>
    <div class="social"><i></i><i></i><i></i><i></i></div>
  </div>
  <div class="vline" style="left:468px"></div>
  <div class="col" style="left:504px">
    <h4>QUICK LINK</h4>
    <ul><li>Contact Us</li><li>Case Studies</li><li>Testimonials</li><li>Certifications</li><li>Membership</li></ul>
  </div>
  <div class="col" style="left:659px;top:66px">
    <ul><li>Site Map</li><li>Support</li><li>Login</li><li>Blog</li></ul>
  </div>
  <div class="vline" style="left:752px"></div>
  <div class="col" style="left:778px">
    <h4>JOIN OUR NEWSLETTER</h4>
    <div class="email-box">E-mail</div>
    <span class="signup">SIGN UP</span>
  </div>
</footer>
<div class="copy">©2018 R.T. Hale Construction . All rights are Reserved</div>

</body>
</html>
```